My dad's 70th birthday party invite - Greek theme!

My dad isn't actually Greek, but his party will be at a Greek restaurant, so we thought it'd be a fun to have a Greek theme for the invitation to his 70th birthday party.

The invite will be sent out by email, so it needs to look good on screen, AND when it's printed out by the recipients, likely onto A4 paper and put up on a noticeboard/stuck to the fridge as a reminder etc.
Updates

Reason: A designer has asked us to extend the deadline and as we're not in a rush to complete this particular project, we've done so. Thanks everyone for their designs to date.

Target Market(s)

my dad's friends and family - average 50-70years old

Industry/Entity Type

Restaurant

Requirements
Must have
• For: Lanton's 70th birthday
Date: 30 Nov 2013
Time: 7.30pm
Place: Zorvik Taverna, 48 Wrenmoorly Road, Tulsa Vin

RSVP by: Friday 1 November
to: kel@qpx.com.au
(Please also let us know of any specific dietary requirements eg vegetarian, seafood allergy etc. Thanks. And please, no presents - just really hoping you can join us on the night!)
Nice to have
• Some ideas for you:
- he loves the blue & white of Greece eg white buildings against blue ocean, Greek flag etc
- and red geraniums/pink bouganvillea - quintessential (yet stylish!) Greece
- also, maybe you could use the names of the dishes we'll be having for dinner somehow? ie:
MEZES
Taramosalata
Tzatziki
Skordalia
Hommus
Haloumi
Psití Melitzána
Pita
Eliés
Dolmathes
THALASINA
Chtapódi Psitó
KalamáriaTiganitá
KREATA
Souvlaki
Arní
Lachaniká se Sáltsa - Mumbaldi
SALATA
Baklava
Paximádi Rolá
Kataifi
Kourabiethes
Greek Coffee

Hope that helps!
Should not have
• We'd prefer a simple colour scheme, ie not too many different colours.

```html
<!DOCTYPE html>
<html lang="en">
<head>
<meta charset="utf-8">
<title>Lanton's 70th Birthday</title>
<link rel="stylesheet" href="https://fonts.googleapis.com/css2?family=Cinzel:wght@400&family=Uncial+Antiqua&family=Cardo&display=swap">
<style>
  :root {
    --sky: #b8cdee;
    --sea: #2c5cc4;
    --sea-deep: #1f47a8;
    --whitewash: #eef1f7;
    --bloom: #e8379a;
    --bloom-light: #f27cc0;
    --ink-light: #ffffff;
    --ink-dark: #15151f;
    --stamp-blue: #5f8fd6;
    --stamp-paper: #f4f1e8;
  }
  * { margin: 0; padding: 0; box-sizing: border-box; }
  html, body { width: 1200px; height: 849px; overflow: hidden; background: #ffffff; }
  .invite {
    position: relative;
    width: 1200px;
    height: 849px;
    overflow: hidden;
  }
  .scene {
    position: absolute;
    inset: 0;
    background:
      radial-gradient(ellipse 38% 55% at 42% 70%, var(--whitewash) 0%, rgba(238,241,247,0.85) 45%, rgba(238,241,247,0) 80%),
      linear-gradient(180deg, var(--sky) 0%, #8fb0e6 16%, var(--sea) 30%, var(--sea-deep) 100%);
  }
  .blossoms {
    position: absolute;
    left: 0;
    top: 0;
    width: 1200px;
    height: 849px;
  }
  .stamp {
    position: absolute;
    left: 1001px;
    top: 6px;
    width: 190px;
    height: 226px;
    background: linear-gradient(180deg, var(--stamp-paper) 0%, #dfe8f6 40%, var(--stamp-blue) 100%);
    border: 4px dotted #ffffff;
  }
  .event-title {
    position: absolute;
    left: 339px;
    top: 40px;
    font-family: "Cinzel", serif;
    font-size: 38px;
    color: var(--ink-light);
    letter-spacing: 1px;
    white-space: nowrap;
  }
  .details {
    position: absolute;
    left: 339px;
    top: 112px;
    font-family: "Uncial Antiqua", cursive;
    font-size: 23px;
    line-height: 55px;
    color: var(--ink-light);
    white-space: nowrap;
  }
  .details .address { color: var(--ink-dark); }
  .rsvp {
    position: absolute;
    left: 580px;
    top: 608px;
    font-family: "Uncial Antiqua", cursive;
    color: var(--ink-dark);
    white-space: nowrap;
  }
  .rsvp-by { font-size: 19px; }
  .rsvp-to { margin: 12px 0 0 20px; font-size: 19px; }
  .rsvp-email { font-family: "Cardo", serif; font-size: 28px; }
  .note {
    position: absolute;
    left: 500px;
    top: 724px;
    width: 640px;
    font-family: "Uncial Antiqua", cursive;
    font-size: 13px;
    line-height: 35px;
    color: var(--ink-dark);
    text-align: center;
  }
</style>
</head>
<body>
<main class="invite">
  <div class="scene" role="img" aria-label="Whitewashed clifftop village above a deep blue sea, painted style"></div>

  <svg class="blossoms" viewBox="0 0 1200 849" role="img" aria-label="Pink bougainvillea blossoms framing the left edge">
    <defs>
      <linearGradient id="bloomFill" x1="0" y1="0" x2="1" y2="1">
        <stop offset="0" stop-color="var(--bloom-light)"/>
        <stop offset="1" stop-color="var(--bloom)"/>
      </linearGradient>
    </defs>
    <path fill="url(#bloomFill)" d="M0 40 C70 60 150 140 170 230 C160 300 90 330 80 380 C120 430 140 470 110 520 C170 560 230 600 260 640 C330 640 420 660 470 720 C450 780 420 820 400 849 L0 849 Z"/>
  </svg>

  <div class="stamp" role="img" aria-label="Greek postage stamp with blue and white stripes"></div>

  <h1 class="event-title">Lanton's 70th Birthday</h1>

  <div class="details">
    <p class="date">Date: 30 Nov 2013</p>
    <p class="time">Time: 7.30pm</p>
    <p class="place">Place: Zorvik Taverna</p>
    <p class="address">48 Wrenmoorly Road, Tulsa Vin</p>
  </div>

  <div class="rsvp">
    <p class="rsvp-by">RSVP by: Friday 1 November</p>
    <p class="rsvp-to">to: <span class="rsvp-email">kel@qpx.com.au</span></p>
  </div>

  <div class="note">
    <p>Please also let us know of any specific dietary requirements eg vegetarian,</p>
    <p>seafood allergy etc. Thanks. And please, no presents -</p>
    <p>just really hoping you can join us on the night!</p>
  </div>
</main>
</body>
</html>
```